Copper Ridge Business Cards For New Startup

I am looking for you to design some business cards for a new startup https://copperridgehub.example. I have supplied logo, brand guidelines and our signatures as a guide.

We need this to reflect the brand guidelines and the website for brand consistency,

What is Copper Ridge?

Mallorca's Business Growth Community
Join your new business community full of passionate entrepreneurs who
love to solve problems and help each other grow together!

Any questions you can ask.

Target Market(s)

Business to Business

Contact Information for Business Card

These are attached (signatures) to the job

Font styles to use
Other font styles liked:
• Open Sans

Requirements
Must have
• Match design guidelines
Nice to have
• Photos of our faces so people remember us

```html
<!DOCTYPE html>
<html lang="en">
<head>
<meta charset="UTF-8">
<title>Copper Ridge — Business Cards</title>
<link href="https://fonts.googleapis.com/css2?family=Lato:wght@300;400;700&display=swap" rel="stylesheet">
<style>
  :root {
    --backdrop: #1b1b1d;
    --card: #131313;
    --card-edge: #1e1e1e;
    --brand-olive: #6e6c14;
    --text-light: #f2f2f2;
    --text-muted: #d4d4d4;
    --rule: #4a4a4a;
    --photo-light: #eef0ec;
    --photo-mid: #c9cfd6;
    --photo-deep: #6f86a6;
  }
  * { box-sizing: border-box; margin: 0; padding: 0; }
  html, body {
    width: 1200px; height: 900px; overflow: hidden;
    background: var(--backdrop);
    font-family: "Lato", "Helvetica Neue", Arial, sans-serif;
  }
  .sheet {
    position: relative; width: 1200px; height: 900px;
    display: flex; align-items: center; justify-content: center; gap: 60px;
  }
  .card {
    position: relative;
    width: 525px; height: 300px;
    background: var(--card);
    border: 1px solid var(--card-edge);
    border-radius: 22px;
    box-shadow: 0 20px 40px rgba(0,0,0,.5);
    overflow: hidden;
  }
  /* Front */
  .card--front { display: flex; align-items: center; justify-content: center; }
  .brand { display: flex; align-items: center; gap: 18px; }
  .brand__mark {
    width: 64px; height: 64px; border-radius: 50%;
    border: 3px solid var(--brand-olive);
  }
  .brand__name {
    color: var(--brand-olive);
    font-size: 34px; font-weight: 700; letter-spacing: 1px;
    text-transform: uppercase;
  }
  /* Back */
  .card--back { display: flex; align-items: flex-start; }
  .portrait {
    position: absolute; left: 40px; top: 70px;
    width: 220px; height: 190px; border-radius: 26px;
    background: linear-gradient(160deg, var(--photo-light) 0%, var(--photo-mid) 55%, var(--photo-deep) 100%);
  }
  .details {
    position: absolute; left: 285px; top: 32px; width: 210px;
    color: var(--text-light);
  }
  .details__name { font-size: 19px; font-weight: 700; text-transform: uppercase; letter-spacing: .3px; }
  .details__role, .details__company { font-size: 13px; font-weight: 300; color: var(--text-muted); line-height: 1.35; }
  .details__rule { height: 1px; background: var(--rule); margin: 12px 0; }
  .contact { list-style: none; font-size: 13px; font-weight: 300; color: var(--text-muted); }
  .contact li { display: flex; align-items: center; gap: 8px; line-height: 1.5; }
  .contact svg { width: 12px; height: 12px; fill: var(--text-light); flex: none; }
  .social { display: flex; gap: 8px; justify-content: center; margin-top: 4px; }
  .social span {
    width: 26px; height: 26px; border-radius: 50%;
    border: 1.5px solid var(--text-light);
  }
</style>
</head>
<body>
  <main class="sheet">
    <section class="card card--front" aria-label="Card front">
      <div class="brand">
        <span class="brand__mark"></span>
        <span class="brand__name">Copper Ridge</span>
      </div>
    </section>

    <section class="card card--back" aria-label="Card back">
      <div class="portrait" role="img" aria-label="Portrait photo of Daniel Marsh"></div>
      <div class="details">
        <h1 class="details__name">Daniel Marsh</h1>
        <p class="details__role">Founder &amp; Growth Hacker</p>
        <p class="details__company">Copper Ridge</p>
        <div class="details__rule"></div>
        <ul class="contact">
          <li>
            <svg viewBox="0 0 24 24" aria-hidden="true"><path d="M6.6 10.8a15.1 15.1 0 006.6 6.6l2.2-2.2a1 1 0 011-.25 11.4 11.4 0 003.6.57 1 1 0 011 1V20a1 1 0 01-1 1A17 17 0 013 4a1 1 0 011-1h3.5a1 1 0 011 1c0 1.25.2 2.45.57 3.6a1 1 0 01-.25 1z"/></svg>
            +34 611 482 907
          </li>
          <li>
            <svg viewBox="0 0 24 24" aria-hidden="true"><path d="M2 5h20v14H2zm2 2v.4l8 5 8-5V7l-8 5z"/></svg>
            dm@copperridgehub.example
          </li>
          <li>
            <svg viewBox="0 0 24 24" aria-hidden="true"><circle cx="12" cy="12" r="10"/></svg>
            www.copperridgehub.example
          </li>
        </ul>
        <div class="details__rule"></div>
        <div class="social" aria-label="Social profiles">
          <span></span><span></span><span></span><span></span><span></span>
        </div>
      </div>
    </section>
  </main>
</body>
</html>
```